Professional Corporate Christmas Card

We require a Christmas card to send to corporate clients on behalf of our Accounting and Financial planning firm.
We like a clean design and our corporate colours are white, blue and silvery grey.
We don't want our logo on the front of the card. We would like something professional and elegant on the front, with the message 'Merry Christmas' or similar.
Our text for the inside of the card is:
Our very best wishes to you this festive season.
May 2014 bring you peace, joy and prosperity.
From the Directors and Staff at Dunmore Group of Companies.
We would like our logo to be subtly placed within the inside of the card - it could have a level of transparency if that helps to gain that effect. It could also be built into the design if you wish. I have attached the logo.
Our website is at http://dunmoregroup-example.com.au/ to give an idea of our corporate style.
**We will be printing through Printlane, so we would like the colours you use to be CYMK**
We will order the card size - 182x117cm (folded)
Thank you for considering the proposal ... we look forward to receiving your designs!
Target Market(s)
The audience of this card is varied: property developers, CEO's, cane farmers, professionals - it will be going to referral sources and our top end clients.
Industry/Entity Type
Printing

```html
<!DOCTYPE html>
<html lang="en">
<head>
<meta charset="utf-8">
<title>Dunmore Group of Companies – Christmas Card</title>
<link rel="stylesheet" href="https://fonts.googleapis.com/css2?family=Great+Vibes&family=Oswald:wght@300&family=Open+Sans:wght@400&display=swap">
<style>
  :root {
    --page-bg: #e9eaec;
    --blue-deep: #0b3384;
    --blue-mid: #1a52ad;
    --blue-light: #2f7fd0;
    --brand-blue: #1b57a8;
    --silver-light: #f4f5f7;
    --silver-mid: #d9dce1;
    --silver-dark: #b9bec6;
    --ink-grey: #4a4d52;
    --white: #ffffff;
  }
  * { box-sizing: border-box; margin: 0; padding: 0; }
  html, body {
    width: 1200px; height: 900px; overflow: hidden;
    background: var(--page-bg);
  }
  .canvas {
    position: relative; width: 1200px; height: 900px;
  }
  .card {
    position: absolute; top: 240px;
    width: 540px; height: 420px;
    box-shadow: 0 10px 30px rgba(0,0,0,.18);
    overflow: hidden;
  }
  /* ---------- Front ---------- */
  .card-front {
    left: 40px;
    background: radial-gradient(ellipse at 50% 50%, var(--blue-light) 0%, var(--blue-mid) 45%, var(--blue-deep) 100%);
  }
  .front-pattern {
    position: absolute; inset: 0;
    background: radial-gradient(circle at 30% 25%, rgba(255,255,255,.06), transparent 60%),
                radial-gradient(circle at 75% 80%, rgba(255,255,255,.05), transparent 55%);
  }
  .ribbon {
    position: absolute; left: 0; right: 0; top: 168px; height: 86px;
    background: linear-gradient(180deg, var(--silver-light) 0%, var(--silver-mid) 55%, var(--silver-dark) 100%);
  }
  .ribbon::before, .ribbon::after {
    content: ""; position: absolute; left: 0; right: 0;
    border-top: 1.5px dashed var(--blue-light);
  }
  .ribbon::before { top: 8px; }
  .ribbon::after { bottom: 8px; }
  .label {
    position: absolute; left: 125px; top: 80px;
    width: 290px; height: 260px;
  }
  .label svg { position: absolute; inset: 0; }
  .greeting {
    position: absolute; inset: 0;
    color: var(--brand-blue); text-align: center;
  }
  .greeting-merry {
    position: absolute; left: 0; right: 0; top: 28px;
    font-family: "Great Vibes", cursive; font-size: 104px; line-height: 1;
  }
  .greeting-christmas {
    position: absolute; left: 0; right: 0; top: 120px;
    font-family: "Oswald", sans-serif; font-weight: 300;
    font-size: 30px; letter-spacing: 1px;
  }
  .greeting-and {
    position: absolute; left: 0; right: 0; top: 152px;
    font-family: "Great Vibes", cursive; font-size: 18px; color: #8a9099;
  }
  .greeting-newyear {
    position: absolute; left: 0; right: 0; top: 160px;
    font-family: "Great Vibes", cursive; font-size: 58px; line-height: 1;
  }
  /* ---------- Inside ---------- */
  .card-inside {
    left: 620px; background: var(--white);
  }
  .inside-message {
    position: absolute; left: 0; right: 0; top: 120px;
    font-family: "Great Vibes", cursive; font-size: 27px; line-height: 39px;
    color: var(--ink-grey); text-align: center;
  }
  .inside-band {
    position: absolute; left: 0; right: 0; bottom: 0; height: 68px;
    background: linear-gradient(90deg, var(--blue-deep), var(--blue-mid) 50%, var(--blue-deep));
  }
  .inside-swoosh { position: absolute; right: 0; bottom: 0; }
  .brand-mark {
    position: absolute; right: 24px; bottom: 24px;
    display: flex; align-items: center; gap: 8px;
    font-family: "Open Sans", sans-serif; font-weight: 400;
    font-size: 30px; color: var(--brand-blue);
  }
  .brand-dot {
    width: 14px; height: 14px; border-radius: 50%;
    background: var(--brand-blue);
  }
</style>
</head>
<body>
<main class="canvas">

  <section class="card card-front" aria-label="Card front">
    <div class="front-pattern" role="img" aria-label="Subtle blue swirl pattern"></div>
    <div class="ribbon"></div>
    <div class="label">
      <svg viewBox="0 0 290 260" width="290" height="260" aria-hidden="true">
        <defs>
          <radialGradient id="labelFill" cx="50%" cy="45%" r="65%">
            <stop offset="0%" stop-color="#ffffff"/>
            <stop offset="70%" stop-color="#eceef1"/>
            <stop offset="100%" stop-color="#c9cdd3"/>
          </radialGradient>
        </defs>
        <path d="M40,0 H250 A40,40 0 0 0 290,40 V220 A40,40 0 0 0 250,260 H40 A40,40 0 0 0 0,220 V40 A40,40 0 0 0 40,0 Z"
              fill="url(#labelFill)" stroke="#aeb3bb" stroke-width="1.5"/>
        <path d="M48,10 H242 A38,38 0 0 0 280,48 V212 A38,38 0 0 0 242,250 H48 A38,38 0 0 0 10,212 V48 A38,38 0 0 0 48,10 Z"
              fill="none" stroke="#b8bdc5" stroke-width="1" stroke-dasharray="2 3"/>
      </svg>
      <div class="greeting">
        <p class="greeting-merry">Merry</p>
        <p class="greeting-christmas">CHRISTMAS</p>
        <p class="greeting-and">and</p>
        <p class="greeting-newyear">New Year</p>
      </div>
    </div>
  </section>

  <section class="card card-inside" aria-label="Card inside">
    <p class="inside-message">
      Our very best wishes to you this festive season.<br>
      May bring you peace, joy and prosperity.<br>
      From the Directors and Staff at<br>
      Dunmore Group of Companies.
    </p>
    <div class="inside-band" role="img" aria-label="Blue band with subtle swirl pattern"></div>
    <svg class="inside-swoosh" width="170" height="80" viewBox="0 0 170 80" aria-hidden="true">
      <path d="M40,80 C0,60 10,0 90,0 H170 V80 Z" fill="#ffffff"/>
    </svg>
    <div class="brand-mark">
      <span class="brand-dot"></span>
      <span class="brand-name">Dunmore</span>
    </div>
  </section>

</main>
</body>
</html>
```